Medical centre needs a business card

We are a medcial centre in Australia, needing a new business card. Our demographic is low working class families. We are going to be renovating our premises to modernise the look and also had a new logo done a few months ago representing quality and community, and now need to update our cards. It needs to be doubled sided, with logo and contact details on the front, and appointment details on the back. . Needs to be modern and simple, easy to read. <br/><br/>Name: Fern Vale Medical Centre <br/>Address: 512 Kestrel Rd (Cnr Kestrel Rd & Lindon Park Rd),<br/>Corvane Court Shopping Centre, Brindlewood, SA 5190<br/>Ph: 08 8361 4027<br/>Tag line: Where every visit counts for you<br/>Website: www.fernvalemedicalcentre.example.au<br/>Online bookings also available<br/><br/>(On the back, to have 3 lines of appointments that can be written in.<br/>Day, date, time)<br/><br/>Your next appointment is on<br/>Can try “M T W Th F Sa Su _________________ at ____________ am/pm” or other combinations <br/>Please advise as soon as possible if unable to attend<br/>Cancellation fees apply if less than 2 hrs notice<br/>Online appointments available (please highlight this option by either by position, colour or font)

Target Market(s)

Lower social economic working class, young families to seniors

Industry/Entity Type

Medical Centre

Contact Information for Business Card

Fern Vale Medical Centre
512 Kestrel Rd (Cnr Kestrel Rd & Lindon Park Drive)
Corvane Court Shopping Centre
Paralowie SA 5108
Ph: 08 8361 4027
www.fernvalemedicalcentre.example.au
Tagline line: where every visit counts for you
Back side is for appointments
Your next appointment is with Dr ______________
Day/date/time (Please give 3 lines of appointments)
Please advise as soon as possible if unable to attend
Cancellation fees apply if less than 2 hours notice
Online appointments available
Book online easily and conveniently (please highlight online appointments)

Font styles to use
Serif
Sans Serif

Colors

Designer to choose colors to be used in the design.

Requirements
Must have
• Modern and simple
• Easy to ready
• Induces a wellbeing feeling
• Incorporate our logo colours and feel from logo
• Induces feeling of stability and security
Nice to have
• Attract attention
• Pleasant to look at
• Feeling of innovation
Should not have
• Loud clashing colours
• Overly luxurious feeling
• Overly artistic

```html
<!DOCTYPE html>
<html lang="en">
<head>
<meta charset="utf-8">
<title>Fern Vale Medical Centre – Business Card</title>
<link rel="stylesheet" href="https://fonts.googleapis.com/css2?family=PT+Sans:ital,wght@0,400;0,700;1,400&display=swap">
<style>
  :root {
    --blue: #0b5cb5;
    --blue-bright: #1f86e0;
    --green: #8cc63f;
    --aqua: #bfeaf7;
    --aqua-soft: #e6f7fc;
    --white: #ffffff;
    --stage: #ecedf0;
    --card-w: 560px;
    --card-h: 320px;
  }
  * { box-sizing: border-box; margin: 0; padding: 0; }
  html, body { width: 1200px; height: 800px; overflow: hidden; }
  body {
    background: var(--stage);
    font-family: "PT Sans", Arial, sans-serif;
    color: var(--blue);
    position: relative;
  }
  .card {
    position: absolute;
    left: 320px;
    width: var(--card-w);
    height: var(--card-h);
    background: var(--white);
    overflow: hidden;
    box-shadow: 0 6px 20px rgba(0,0,0,0.12);
  }
  .card--front { top: 50px; }
  .card--back { top: 430px; }

  .edge-band { position: absolute; top: 0; left: 0; width: 100%; height: 100%; pointer-events: none; }

  .backdrop-wash {
    position: absolute; inset: 0;
    background: radial-gradient(ellipse 75% 80% at 0% 100%, var(--aqua) 0%, var(--aqua-soft) 45%, rgba(255,255,255,0) 100%);
  }

  /* Front */
  .brand { position: absolute; left: 60px; top: 70px; }
  .brand__name {
    display: flex; align-items: center; gap: 10px;
    font-size: 27px; font-weight: 700; color: var(--blue);
    letter-spacing: 0.5px; text-transform: uppercase;
  }
  .brand__mark { width: 16px; height: 16px; background: var(--green); }
  .brand__tagline {
    margin-top: 6px; margin-left: 26px;
    font-size: 14px; letter-spacing: 1.6px; color: var(--blue);
  }
  .contact { position: absolute; right: 26px; bottom: 40px; text-align: right; }
  .contact__row {
    display: flex; align-items: center; justify-content: flex-end; gap: 10px;
    margin-top: 6px;
  }
  .contact__text { font-size: 13px; line-height: 1.2; color: var(--blue); }
  .contact__text--phone { font-size: 20px; font-weight: 700; }
  .contact__text--web { font-size: 14px; font-weight: 700; }
  .contact__icon {
    width: 26px; height: 26px; flex: none;
    background: var(--blue); border-radius: 3px;
    display: flex; align-items: center; justify-content: center;
  }

  /* Back */
  .appointment { position: absolute; left: 34px; top: 26px; right: 30px; }
  .appointment__title { font-size: 19px; display: flex; align-items: flex-end; gap: 6px; }
  .fill-line { flex: 1; border-bottom: 1px solid var(--blue); height: 18px; }
  .days { display: flex; gap: 20px; margin-top: 10px; font-size: 18px; }
  .day { display: flex; align-items: center; gap: 5px; }
  .day::before { content: ""; width: 10px; height: 10px; border: 1px solid var(--blue); }
  .slot { display: flex; align-items: flex-end; gap: 6px; margin-top: 12px; font-size: 18px; }
  .slot::before { content: ""; width: 12px; height: 12px; border-radius: 50%; background: var(--blue); margin-bottom: 4px; }
  .slot__date { flex: 1.3; border-bottom: 1px solid var(--blue); height: 18px; }
  .slot__time { flex: 1; border-bottom: 1px solid var(--blue); height: 18px; }
  .notes { margin-top: 16px; font-size: 16px; line-height: 1.35; }
  .online-pill {
    display: inline-block; margin-top: 10px;
    background: var(--blue); color: var(--white);
    font-size: 15px; font-weight: 700; letter-spacing: 1px;
    padding: 5px 26px; border-radius: 14px; text-transform: uppercase;
  }
</style>
</head>
<body>

<section class="card card--front" aria-label="Business card front">
  <div class="backdrop-wash" role="img" aria-label="Soft light-blue medical background wash"></div>
  <svg class="edge-band" viewBox="0 0 560 320" aria-hidden="true">
    <path d="M0 0 H560 V8 H70 Q20 8 0 40 Z" fill="var(--blue-bright)"/>
    <rect x="300" y="0" width="110" height="8" fill="var(--green)"/>
  </svg>

  <div class="brand">
    <div class="brand__name"><span class="brand__mark"></span>Fern Vale Medical Centre</div>
    <div class="brand__tagline">Where every visit counts for you</div>
  </div>

  <div class="contact">
    <div class="contact__row">
      <span class="contact__text contact__text--phone">08 8361 4027</span>
      <span class="contact__icon"><svg width="16" height="16" viewBox="0 0 24 24"><path d="M6.6 10.8a15 15 0 0 0 6.6 6.6l2.2-2.2c.3-.3.7-.4 1-.2 1.1.4 2.3.6 3.6.6.6 0 1 .4 1 1V20c0 .6-.4 1-1 1A17 17 0 0 1 3 4c0-.6.4-1 1-1h3.5c.6 0 1 .4 1 1 0 1.3.2 2.5.6 3.6.1.3 0 .7-.2 1z" fill="#fff"/></svg></span>
    </div>
    <div class="contact__row">
      <span class="contact__text">hello@fernvale.example.au</span>
      <span class="contact__icon"><svg width="16" height="16" viewBox="0 0 24 24"><rect x="3" y="5" width="18" height="14" fill="none" stroke="#fff" stroke-width="2"/><path d="M3 6l9 7 9-7" fill="none" stroke="#fff" stroke-width="2"/></svg></span>
    </div>
    <div class="contact__row">
      <span class="contact__text contact__text--web">www.fernvalemedicalcentre.example.au</span>
      <span class="contact__icon"><svg width="16" height="16" viewBox="0 0 24 24" fill="none" stroke="#fff" stroke-width="1.6"><circle cx="12" cy="12" r="9"/><ellipse cx="12" cy="12" rx="4" ry="9"/><path d="M3 12h18M5 7h14M5 17h14"/></svg></span>
    </div>
    <div class="contact__row">
      <span class="contact__text">512 Kestrel Rd (Cnr Kestrel Rd &amp; Lindon Park Drive)<br>Corvane Court Shopping Centre, Brindlewood, SA 5190</span>
      <span class="contact__icon"><svg width="16" height="16" viewBox="0 0 24 24"><path d="M12 2a7 7 0 0 0-7 7c0 5 7 13 7 13s7-8 7-13a7 7 0 0 0-7-7z" fill="#fff"/><circle cx="12" cy="9" r="2.5" fill="var(--blue)"/></svg></span>
    </div>
  </div>
</section>

<section class="card card--back" aria-label="Business card back">
  <div class="backdrop-wash" role="img" aria-label="Soft light-blue medical background wash"></div>
  <svg class="edge-band" viewBox="0 0 560 320" aria-hidden="true">
    <path d="M0 0 H560 V8 H70 Q20 8 0 40 Z" fill="var(--blue-bright)"/>
    <rect x="300" y="0" width="110" height="8" fill="var(--green)"/>
  </svg>

  <div class="appointment">
    <div class="appointment__title">Your next appointment is with: Dr. <span class="fill-line"></span></div>
    <div class="days">
      <span class="day">Mon</span><span class="day">Tue</span><span class="day">Wed</span><span class="day">Thu</span><span class="day">Fri</span><span class="day">Sat</span><span class="day">Sun</span>
    </div>
    <div class="slot">Date: <span class="slot__date"></span> Time: <span class="slot__time"></span> am/pm</div>
    <div class="slot">Date: <span class="slot__date"></span> Time: <span class="slot__time"></span> am/pm</div>
    <div class="slot">Date: <span class="slot__date"></span> Time: <span class="slot__time"></span> am/pm</div>
    <p class="notes">Please advise as soon as possible if unable to attend<br>Cancellation fees apply if less than 2 hours notice</p>
    <span class="online-pill">Online appointments available</span>
  </div>
</section>

</body>
</html>
```